New Print Material Needed for Renovation Company

We are looking to update our current Print Material to reflect the current process we offer to our clients. A lot of the information is also outdated along with many of the photos that are currently being used. We are a renovation company that specializes in residential and commercial renovations and custom builds.This project is MULTIPLE pages. We will pay the chosen designer an extra fee for the designing 3-4 additional pages that are similar to the chosen design. Attached is our current Print Material. We are hoping to update the look of them and some of the messaging. Our current company colors are white, blue and light grey and it will remain that way.

Industry/Entity Type

Construction Company

Font styles to use
Sans Serif

Colors
3176b5
ffffff

Requirements
Must have
• Easy to explain the process
• Easy to read and understand let alone
• Easy to navigate
Nice to have
• As much creativity as possible
Should not have
• no confusing text
• no confusing layout

```html
<!DOCTYPE html>
<html lang="en">
<head>
<meta charset="utf-8">
<title>Master Builder Timeline – Harbourline Renovations</title>
<link href="https://fonts.googleapis.com/css2?family=Open+Sans:wght@400;600&display=swap" rel="stylesheet">
<style>
  :root {
    --brand-blue: #1155d4;
    --white: #ffffff;
    --ink: #111111;
    --pale-blue: #e1ebf7;
    --backdrop: #778a8a;
    --frame-line: #333333;
  }
  * { box-sizing: border-box; margin: 0; padding: 0; }
  html, body { width: 1200px; height: 1200px; overflow: hidden; }
  body { background: var(--backdrop); font-family: "Open Sans", sans-serif; position: relative; }

  .sheet {
    position: absolute; left: 106px; top: 217px; width: 989px; height: 766px;
    background: var(--white); box-shadow: 3px 4px 0 rgba(0,0,0,.18);
  }

  .masthead {
    position: absolute; left: 7px; top: 9px; width: 973px; height: 180px;
    background: var(--brand-blue); color: var(--white);
  }
  .masthead__badge {
    position: absolute; left: 27px; top: 55px; width: 88px; height: 88px;
  }
  .masthead__title {
    position: absolute; left: 148px; top: 72px; font-weight: 600; font-size: 40px;
    letter-spacing: -0.2px; line-height: 1; white-space: nowrap;
  }
  .masthead__brand {
    position: absolute; left: 728px; top: 62px; display: flex; align-items: center; gap: 12px;
  }
  .masthead__brand-dot { width: 56px; height: 56px; border: 5px solid var(--white); border-radius: 50%; flex: none; }
  .masthead__brand-name { font-size: 20px; font-weight: 400; line-height: 1.15; width: 140px; }

  .phase { position: absolute; top: 258px; width: 330px; height: 380px; }
  .phase--design { left: 23px; }
  .phase--plan { left: 345px; }
  .phase--build { left: 685px; }

  .phase__emblem { position: absolute; left: 90px; top: -25px; width: 110px; height: 100px; }

  .phase__ribbon { position: absolute; left: 0; top: 86px; width: 28px; height: 279px; }

  .phase__card {
    position: absolute; left: 34px; top: 79px; width: 244px; height: 295px;
    border: 1px solid var(--frame-line); background: var(--white);
  }
  .step { position: absolute; left: 12px; right: 8px; }
  .step--1 { top: 20px; }
  .step--2 { top: 119px; }
  .step--3 { top: 218px; }
  .step__heading { font-size: 14.5px; font-weight: 400; color: var(--ink); line-height: 1.2; margin-bottom: 6px; white-space: nowrap; }
  .step__body { font-size: 9px; line-height: 15px; text-transform: uppercase; color: var(--ink); letter-spacing: -0.1px; }

  .footer-band { position: absolute; left: 0; bottom: 0; width: 100%; height: 55px; background: var(--pale-blue); }
  .footer-tag { position: absolute; left: 588px; top: 10px; width: 392px; height: 35px; }
  .footer-tag svg { position: absolute; left: 0; top: 0; }
  .footer-tag__text {
    position: absolute; left: 54px; top: 3px; color: var(--white); font-size: 20px; letter-spacing: -0.6px; white-space: nowrap;
  }
</style>
</head>
<body>
<main class="sheet">

  <header class="masthead">
    <div class="masthead__badge" role="img" aria-label="Tools badge emblem">
      <svg width="88" height="88" viewBox="0 0 88 88"><circle cx="44" cy="44" r="40" fill="none" stroke="#fff" stroke-width="3"/><circle cx="44" cy="44" r="30" fill="none" stroke="#fff" stroke-width="2"/></svg>
    </div>
    <h1 class="masthead__title">MASTER BUIDER TIMELINE</h1>
    <div class="masthead__brand">
      <span class="masthead__brand-dot"></span>
      <span class="masthead__brand-name">Harbourline Renovations</span>
    </div>
  </header>

  <section class="phase phase--design">
    <svg class="phase__emblem" viewBox="0 0 110 100">
      <defs><path id="arc-design" d="M15 62 A40 40 0 0 1 95 62"/></defs>
      <text font-family="Open Sans, sans-serif" font-size="19" fill="#1155d4" text-anchor="middle"><textPath href="#arc-design" startOffset="50%">DESIGN</textPath></text>
      <circle cx="55" cy="62" r="33" fill="#1155d4" role="img" aria-label="Collaboration icon of two clients exchanging ideas"/>
    </svg>
    <svg class="phase__ribbon" viewBox="0 0 28 279"><polygon points="0,0 28,23 28,279 0,256" fill="#1155d4"/>
      <g fill="#fff" font-family="Open Sans, sans-serif" font-weight="600" font-size="20" text-anchor="middle"><text x="14" y="35">1</text><text x="14" y="137">2</text><text x="14" y="235">3</text></g></svg>
    <div class="phase__card">
      <div class="step step--1"><h2 class="step__heading">INITIAL DESIGN MEETING</h2><p class="step__body">Lorem ipsum dolor sit amet, consectetur adipiscing elit, sed do eiusmod tempor incidi-dunt ut labore et dolore magna aliqua. Quis</p></div>
      <div class="step step--2"><h2 class="step__heading">SECOND DESIGN MEETING</h2><p class="step__body">Lorem ipsum dolor sit amet, consectetur adipiscing elit, sed do eiusmod tempor incidi-dunt ut labore et dolore magna aliqua. Quis</p></div>
      <div class="step step--3"><h2 class="step__heading">FINAL DESIGN MEETING</h2><p class="step__body">Lorem ipsum dolor sit amet, consectetur adipiscing elit, sed do eiusmod tempor incidi-dunt ut labore et dolore magna aliqua. Quis</p></div>
    </div>
  </section>

  <section class="phase phase--plan">
    <svg class="phase__emblem" viewBox="0 0 110 100">
      <defs><path id="arc-plan" d="M15 62 A40 40 0 0 1 95 62"/></defs>
      <text font-family="Open Sans, sans-serif" font-size="19" fill="#1155d4" text-anchor="middle"><textPath href="#arc-plan" startOffset="50%">PLAN</textPath></text>
      <circle cx="55" cy="62" r="33" fill="#1155d4"/>
      <circle cx="55" cy="62" r="25" fill="none" stroke="#fff" stroke-width="2.5"/>
      <g fill="none" stroke="#fff" stroke-width="2.5" stroke-linecap="round">
        <path d="M40 52 l3 3 l5 -6"/><path d="M52 52 h16"/>
        <path d="M40 62 l3 3 l5 -6"/><path d="M52 62 h16"/>
        <path d="M40 72 l3 3 l5 -6"/><path d="M52 72 h16"/>
      </g>
    </svg>
    <svg class="phase__ribbon" viewBox="0 0 28 279"><polygon points="0,0 28,23 28,279 0,256" fill="#1155d4"/>
      <g fill="#fff" font-family="Open Sans, sans-serif" font-weight="600" font-size="20" text-anchor="middle"><text x="14" y="45">1</text><text x="14" y="133">2</text><text x="14" y="230">3</text></g></svg>
    <div class="phase__card">
      <div class="step step--1"><h2 class="step__heading">INITIAL DESIGN MEETING</h2><p class="step__body">Lorem ipsum dolor sit amet, consectetur adipiscing elit, sed do eiusmod tempor incidi-dunt ut labore et dolore magna aliqua. Quis</p></div>
      <div class="step step--2"><h2 class="step__heading">SECOND DESIGN MEETING</h2><p class="step__body">Lorem ipsum dolor sit amet, consectetur adipiscing elit, sed do eiusmod tempor incidi-dunt ut labore et dolore magna aliqua. Quis</p></div>
      <div class="step step--3"><h2 class="step__heading">FINAL DESIGN MEETING</h2><p class="step__body">Lorem ipsum dolor sit amet, consectetur adipiscing elit, sed do eiusmod tempor incidi-dunt ut labore et dolore magna aliqua. Quis</p></div>
    </div>
  </section>

  <section class="phase phase--build">
    <svg class="phase__emblem" viewBox="0 0 110 100">
      <defs><path id="arc-build" d="M15 62 A40 40 0 0 1 95 62"/></defs>
      <text font-family="Open Sans, sans-serif" font-size="19" fill="#1155d4" text-anchor="middle"><textPath href="#arc-build" startOffset="50%">BUILD</textPath></text>
      <circle cx="55" cy="62" r="33" fill="#1155d4"/>
      <circle cx="55" cy="62" r="25" fill="none" stroke="#fff" stroke-width="2.5"/>
      <g fill="#fff">
        <rect x="41" y="69" width="4" height="6"/><rect x="47" y="66" width="4" height="9"/>
        <rect x="53" y="63" width="4" height="12"/><rect x="59" y="59" width="4" height="16"/>
        <rect x="65" y="55" width="4" height="20"/>
      </g>
      <path d="M40 65 Q56 61 64 47" fill="none" stroke="#fff" stroke-width="2.5"/>
      <polygon points="60,45 69,42 67,51" fill="#fff"/>
    </svg>
    <svg class="phase__ribbon" viewBox="0 0 28 279"><polygon points="0,0 28,23 28,279 0,256" fill="#1155d4"/>
      <g fill="#fff" font-family="Open Sans, sans-serif" font-weight="600" font-size="20" text-anchor="middle"><text x="14" y="40">1</text><text x="14" y="135">2</text><text x="14" y="232">3</text></g></svg>
    <div class="phase__card">
      <div class="step step--1"><h2 class="step__heading">INITIAL DESIGN MEETING</h2><p class="step__body">Lorem ipsum dolor sit amet, consectetur adipiscing elit, sed do eiusmod tempor incidi-dunt ut labore et dolore magna aliqua. Quis</p></div>
      <div class="step step--2"><h2 class="step__heading">SECOND DESIGN MEETING</h2><p class="step__body">Lorem ipsum dolor sit amet, consectetur adipiscing elit, sed do eiusmod tempor incidi-dunt ut labore et dolore magna aliqua. Quis</p></div>
      <div class="step step--3"><h2 class="step__heading">FINAL DESIGN MEETING</h2><p class="step__body">Lorem ipsum dolor sit amet, consectetur adipiscing elit, sed do eiusmod tempor incidi-dunt ut labore et dolore magna aliqua. Quis</p></div>
    </div>
  </section>

  <footer class="footer-band">
    <div class="footer-tag">
      <svg width="392" height="35" viewBox="0 0 392 35"><polygon points="0,0 343,0 392,35 42,35" fill="#1155d4"/></svg>
      <span class="footer-tag__text">Harbourline Renovations</span>
    </div>
  </footer>

</main>
</body>
</html>
```